Creation of a personal presentation for Field-Bursaries Norvale

Dear designers
I recently discovered a brochure from a competitor and we would like to develop a similar presentation for our purposes. It is important to emphasize that we do not want an exact copy of the brochure found. Instead, we want to adopt or tweak certain design elements to create a similar feel. Attached you will find detailed instructions, pictures and further information on how to carry out the order.
Please note that the attached Word file contains detailed instructions on how to create the brochure. This guide gives you clear guidelines on how we envision the end result.
We encourage you to use your creativity and incorporate these design elements to create a unique brochure for our company. We look forward to your suggestions and ideas that meet our requirements.
Thank you in advance for your efforts. We are curious about your designs and look forward to working with you.
Updates
Urlaub/Ferien
Target Market(s)
Young footballers between the ages of 17 and 20
Industry/Entity Type
Fussball und Bildung
Look and feel
Each slider illustrates characteristics of the customer's brand and the style your logo design should communicate.

```html
<!DOCTYPE html>
<html lang="de">
<head>
<meta charset="utf-8">
<title>Field-Bursaries Norvale – Präsentation</title>
<link rel="stylesheet" href="https://fonts.googleapis.com/css2?family=Bebas+Neue&family=Montserrat:ital,wght@0,400;0,500;0,600;0,700;0,800;1,500;1,800&display=swap">
<style>
:root{
  --red:#d30a0a;
  --red-deep:#5a0000;
  --red-mid:#9c0202;
  --ink:#111;
  --grey:#4a4a4a;
  --white:#fff;
}
*{margin:0;padding:0;box-sizing:border-box}
html,body{width:1200px;height:939px;overflow:hidden;background:var(--white)}
body{position:relative;font-family:'Montserrat',sans-serif;color:var(--ink)}
.page-label{position:absolute;font-weight:700;font-size:24px;line-height:1;color:#000}
.abs{position:absolute}

/* Page 1 – cover */
.cover{left:24px;top:45px;width:566px;height:437px;overflow:hidden;
  background:radial-gradient(ellipse at 55% 60%,#e10d0d 0%,var(--red) 25%,var(--red-mid) 65%,var(--red-deep) 100%)}
.cover-glow{left:0;top:92px;width:156px;height:33px;background:linear-gradient(90deg,rgba(255,255,255,.85),rgba(255,255,255,0))}
.cover-rule-v{left:518px;top:0;width:4px;height:190px;background:linear-gradient(180deg,rgba(255,255,255,.9),rgba(255,255,255,0))}
.cover-rule-h{left:0;top:276px;width:210px;height:4px;background:linear-gradient(90deg,rgba(255,255,255,.95),rgba(255,255,255,.4))}
.cover-photo{left:93px;top:74px;width:157px;height:187px;border:4px solid var(--white);border-radius:80px 80px 0 0;
  background:linear-gradient(160deg,#3f6a2e 0%,#c9c9cf 45%,#f2f2f4 70%,#2b2c4a 100%)}
.ball-badge{left:206px;top:246px;width:52px;height:52px;border-radius:50%;background:var(--white);display:flex;align-items:center;justify-content:center}
.name{left:272px;top:101px;font-style:italic;font-weight:800;font-size:18px;color:var(--white);letter-spacing:.3px}
.sport{left:272px;top:122px;font-style:italic;font-weight:500;font-size:12.5px;color:var(--white);letter-spacing:1px}
.title{left:272px;top:147px;font-family:'Bebas Neue',sans-serif;font-size:32px;line-height:34px;color:var(--white);letter-spacing:2px}
.tagline{left:273px;top:230px;font-weight:600;font-size:13px;color:var(--white)}
.cta{left:267px;top:250px;padding:2px 6px;background:var(--white);border-radius:3px;font-weight:800;font-size:13px;color:var(--red)}
.press{left:102px;top:307px;width:361px;height:98px;background:var(--white);border-radius:8px}
.press-title{position:absolute;top:9px;left:0;width:100%;text-align:center;font-weight:500;font-size:9.5px;color:var(--grey)}
.press-title::after{content:"";display:block;width:12px;height:1px;background:var(--red);margin:5px auto 0}
.press-grid{position:absolute;left:14px;top:38px;width:333px;display:grid;grid-template-columns:repeat(5,1fr);row-gap:16px}
.press-name{font-weight:600;font-size:7.5px;color:#1d3b7a;text-align:center;display:flex;align-items:center;justify-content:center;gap:3px}
.press-name i{display:inline-block;width:5px;height:5px;background:#1d3b7a}

/* Page 2 – about */
.about{left:602px;top:45px;width:565px;height:437px}
.tab{position:absolute;left:0;width:33px;background:linear-gradient(180deg,var(--red),var(--red-mid))}
.d-photo{position:absolute;left:4px;width:124px;height:103px;border-radius:0 52px 52px 0}
.block{position:absolute;left:144px;width:180px}
.block h3{font-weight:700;font-size:9.5px;color:var(--red);margin-bottom:8px}
.block ul{list-style:none}
.block li{position:relative;padding-left:12px;font-size:7.4px;line-height:8.6px;color:#222;margin-bottom:7px}
.block li::before{content:"";position:absolute;left:0;top:2px;width:5px;height:5px;border-radius:50%;background:var(--red)}
.about-panel{left:924px;top:45px;width:243px;height:437px;background:linear-gradient(180deg,var(--red-deep),var(--red-mid) 45%,var(--red))}
.about-title{position:absolute;right:33px;top:172px;text-align:right;font-family:'Bebas Neue',sans-serif;font-size:28px;line-height:31px;color:var(--white);letter-spacing:2px}
.about-rule{position:absolute;left:0;top:253px;width:124px;height:2px;background:var(--white)}

/* Page 3 – gallery */
.gallery{left:325px;top:494px;width:565px;height:437px;overflow:hidden;
  background:linear-gradient(180deg,var(--red-mid),var(--red) 50%,var(--red-mid))}
.tile{position:absolute;border:3px solid var(--white);border-radius:22px}
</style>
</head>
<body>

<div class="page-label" style="left:25px;top:14px">Page 1</div>
<div class="page-label" style="left:601px;top:14px">Page 2</div>
<div class="page-label" style="left:235px;top:502px">Page 3</div>

<!-- Page 1 -->
<section class="cover abs">
  <div class="cover-glow abs"></div>
  <div class="cover-rule-v abs"></div>
  <div class="cover-rule-h abs"></div>
  <div class="cover-photo abs" role="img" aria-label="Zwei jubelnde Fussballspieler in weissen Trikots"></div>
  <div class="ball-badge abs">
    <svg width="40" height="40" viewBox="0 0 40 40">
      <circle cx="20" cy="20" r="17" fill="#fff" stroke="#d30a0a" stroke-width="3"/>
      <polygon points="20,13 26,17.5 24,24.5 16,24.5 14,17.5" fill="#d30a0a"/>
      <path d="M20 13V5M26 17.5l8-3M24 24.5l5 7M16 24.5l-5 7M14 17.5l-8-3" stroke="#d30a0a" stroke-width="2" fill="none"/>
    </svg>
  </div>
  <div class="name abs">MARCO LENTI</div>
  <div class="sport abs">FUSSBALL</div>
  <div class="title abs">FIELD-BURSARIES<br>NORVALE</div>
  <div class="tagline abs">DEIN WEG IN DEN SPITZENFUSSBALL</div>
  <div class="cta abs">BEGINNT HIER!</div>
  <div class="press abs">
    <div class="press-title">Bekannt aus der Presse</div>
    <div class="press-grid">
      <span class="press-name">Kreisball</span>
      <span class="press-name">Talbote</span>
      <span class="press-name">Flussblatt</span>
      <span class="press-name">Kanal Ost</span>
      <span class="press-name"><i></i>Kreisball</span>
      <span class="press-name">Stadtlook</span>
      <span class="press-name">Quellpost</span>
      <span class="press-name">Bergecho</span>
      <span class="press-name">Seenetz</span>
      <span class="press-name"><i></i>Kreisball</span>
    </div>
  </div>
</section>

<!-- Page 2 -->
<section class="about abs">
  <div class="tab" style="top:0;height:28px"></div>
  <div class="tab" style="top:140px;height:22px"></div>
  <div class="tab" style="top:274px;height:22px"></div>
  <div class="tab" style="top:409px;height:28px"></div>

  <div class="d-photo" style="top:32px;background:linear-gradient(120deg,#2b2f52,#4f6d3a 50%,#8aa86a)" role="img" aria-label="Zwei Spieler im Zweikampf am Ball"></div>
  <div class="d-photo" style="top:166px;background:linear-gradient(130deg,#b81414,#5a1010 55%,#2a2a2a)" role="img" aria-label="Fans mit roter Fahne im Stadion"></div>
  <div class="d-photo" style="top:300px;background:linear-gradient(130deg,#8a2a1a,#c9a84a 50%,#2a2620)" role="img" aria-label="Jubelnde Mannschaft nach dem Spiel"></div>

  <div class="block" style="top:32px">
    <h3>DER MARKTFÜHRER</h3>
    <ul>
      <li>Die Nummer 1 in Norvale</li>
      <li>20 Jahre Erfahrung in der Vermittlung von Sport-Stipendien</li>
      <li>Über 2000 vermittelte Athleten</li>
      <li>Bewertung von 5,0 Sternen auf Rateport Rezensionen</li>
      <li>Bekannt aus der Presse</li>
    </ul>
  </div>
  <div class="block" style="top:166px;width:184px">
    <h3>FUSSBALLSTIPENDIEN</h3>
    <ul>
      <li>Partnerschaft mit über 1500 Universitäten</li>
      <li>Über 1000 zufriedene Kunden</li>
      <li>Grösstes Fussball-Showcase in Europa und regelmässige Trainerbesuche in Norvale</li>
      <li>Rating of 5.0 stars on Rateport Reviews</li>
      <li>Known from the press</li>
    </ul>
  </div>
  <div class="block" style="top:304px;width:176px">
    <h3>DAS EXPERTENTEAM</h3>
    <ul>
      <li>Qualitativ herausragende und umfassende Beratung mit Experten in allen Bereichen des Prozesses</li>
      <li>Gründungsmitglied des GLOBAL COUNCIL for Sport &amp; Study Excellence</li>
    </ul>
  </div>
</section>

<section class="about-panel abs">
  <div class="about-title">ÜBER<br>FIELD-BURSARIES<br>NORVALE</div>
  <div class="about-rule"></div>
</section>

<!-- Page 3 -->
<section class="gallery abs">
  <div class="tile" style="left:0;top:-20px;width:136px;height:96px;background:linear-gradient(180deg,#2a2a2a,#4d7a3a)" role="img" aria-label="Football-Stadion von oben"></div>
  <div class="tile" style="left:0;top:85px;width:136px;height:184px;background:linear-gradient(180deg,#8fb5d8,#4f7a3a 55%,#c9c2b2)" role="img" aria-label="Campusweg mit Palmen"></div>
  <div class="tile" style="left:0;top:276px;width:136px;height:180px;background:linear-gradient(180deg,#9cc4e6,#3f7a3a 50%,#7a6a5a)" role="img" aria-label="Studierende auf dem Campus"></div>

  <div class="tile" style="left:143px;top:-20px;width:135px;height:138px;background:linear-gradient(160deg,#3f6a2e,#e8e8ec 50%,#2b2c4a)" role="img" aria-label="Zwei jubelnde Spieler"></div>
  <div class="tile" style="left:143px;top:126px;width:135px;height:184px;background:linear-gradient(140deg,#c21414,#4a1010 55%,#222)" role="img" aria-label="Fans mit Fahne im Stadion"></div>
  <div class="tile" style="left:143px;top:317px;width:135px;height:140px;background:linear-gradient(180deg,#6a7a6a,#4a8a3a)" role="img" aria-label="Fussballhalle"></div>

  <div class="tile" style="left:286px;top:-20px;width:135px;height:138px;background:linear-gradient(120deg,#2b2f52,#4f6d3a 50%,#7a9a5a)" role="img" aria-label="Zweikampf am Ball"></div>
  <div class="tile" style="left:286px;top:126px;width:135px;height:184px;background:linear-gradient(150deg,#5a4a6a,#e8d8c8 45%,#8a1a1a)" role="img" aria-label="Spieler umarmen sich"></div>
  <div class="tile" style="left:286px;top:317px;width:135px;height:140px;background:linear-gradient(180deg,#5a2a2a,#2a3a2a 55%,#3a7a3a)" role="img" aria-label="Spieler beim Schuss"></div>

  <div class="tile" style="left:429px;top:-20px;width:136px;height:96px;background:linear-gradient(180deg,#c8ccd0,#5a9ab0 60%,#5a5a5a)" role="img" aria-label="Schwimmhalle"></div>
  <div class="tile" style="left:429px;top:85px;width:136px;height:184px;background:linear-gradient(150deg,#8a7a3a,#d8c890 45%,#2a2620)" role="img" aria-label="Jubelnde Mannschaft"></div>
  <div class="tile" style="left:429px;top:276px;width:136px;height:180px;background:linear-gradient(180deg,#6a5a5a,#c8c0c0 50%,#8a3a1a)" role="img" aria-label="Spieler beim Freistoss"></div>
</section>

</body>
</html>
```